Uprising SaaS company needs an attractive business card design

We're an uprising SaaS company who's attempting to attack the rigid car (insurance) claims management market in Europe.
We want to our mighty base order management system, listen to our clients to connect the smart ideas to build something even mightier.
We primarily focus on helping our customers manage their customers' claims/orders and get them resolved as smoothly as possible.
We'd like the business card design to express technical innovation and the fact that we connect smart ideas, as our company slogan indicates.
Contact Information for Business Card
Name, position, website, email, mobile, business address
Colors
Designer to choose colors to be used in the design.
Look and feel
Each slider illustrates characteristics of the customer's brand and the style your logo design should communicate.

```html
<!DOCTYPE html>
<html lang="en">
<head>
<meta charset="utf-8">
<title>Nexoria – Business Card</title>
<link href="https://fonts.googleapis.com/css2?family=Montserrat:wght@400;500;700&display=swap" rel="stylesheet">
<style>
  :root {
    --backdrop: #141414;
    --card: #ffffff;
    --sky: #82d0e4;
    --graphite: #7b7b7b;
    --ink: #6f6f6f;
    --white: #ffffff;
  }
  * { margin: 0; padding: 0; box-sizing: border-box; }
  html, body {
    width: 1200px; height: 728px; overflow: hidden;
    background: var(--backdrop);
    font-family: "Montserrat", sans-serif;
  }
  .canvas { position: relative; width: 1200px; height: 728px; }
  .card {
    position: absolute; top: 212px;
    width: 507px; height: 303px;
    background: var(--card);
    overflow: hidden;
  }
  .card--front { left: 74px; }
  .card--back { left: 620px; }
  .card__waves { position: absolute; inset: 0; width: 100%; height: 100%; }

  .wordmark {
    position: absolute;
    color: var(--graphite);
    font-weight: 400;
    line-height: 1;
    letter-spacing: 0.5px;
  }
  .card--front .wordmark { left: 43px; top: 64px; font-size: 36px; }
  .card--back .wordmark { left: 142px; top: 206px; font-size: 46px; }

  .identity {
    position: absolute; right: 37px; top: 56px;
    text-align: right;
  }
  .identity__name {
    font-size: 20px; font-weight: 700; color: var(--ink);
    letter-spacing: 0.6px; line-height: 1;
  }
  .identity__name span { color: var(--sky); }
  .identity__role {
    margin-top: 5px;
    font-size: 12px; font-weight: 400; color: var(--ink);
  }

  .contacts {
    position: absolute; left: 37px; top: 204px;
    list-style: none;
  }
  .contacts li {
    display: flex; align-items: center; gap: 5px;
    color: var(--white); font-size: 15px; font-weight: 400;
    height: 24px;
  }
  .contacts svg { width: 14px; height: 14px; flex: none; }

  .slogan {
    position: absolute; left: 204px; top: 70px;
    color: var(--white); font-size: 18.5px; font-weight: 500;
    letter-spacing: 0.5px;
  }
</style>
</head>
<body>
<main class="canvas">

  <section class="card card--front">
    <svg class="card__waves" viewBox="0 0 507 303" preserveAspectRatio="none" aria-hidden="true">
      <path d="M0 175 C110 137 262 168 404 303 L0 303 Z" fill="var(--graphite)"/>
      <path d="M0 180 C110 144 256 175 392 303 L0 303 Z" fill="var(--card)"/>
      <path d="M0 184 C110 150 250 182 380 303 L0 303 Z" fill="var(--sky)"/>
    </svg>

    <div class="wordmark">nexoria</div>

    <div class="identity">
      <div class="identity__name">MARA <span>LINDQVIST</span></div>
      <div class="identity__role">CEO/Owner</div>
    </div>

    <ul class="contacts">
      <li>
        <svg viewBox="0 0 14 14" aria-hidden="true"><circle cx="7" cy="7" r="7" fill="var(--white)"/><path d="M4.3 3.6l1.4-.3.8 1.8-.9.7c.4.9 1.1 1.6 2 2l.7-.9 1.8.8-.3 1.4c-3 .2-5.7-2.5-5.5-5.5z" fill="var(--sky)"/></svg>
        (555) 214-0187
      </li>
      <li>
        <svg viewBox="0 0 14 14" aria-hidden="true"><circle cx="7" cy="7" r="7" fill="var(--white)"/><rect x="3.5" y="4.6" width="7" height="4.8" fill="none" stroke="var(--sky)" stroke-width="1"/><path d="M3.5 4.6L7 7.4l3.5-2.8M3.5 9.4L6 7M10.5 9.4L8 7" fill="none" stroke="var(--sky)" stroke-width="0.9"/></svg>
        info@nexoria.com
      </li>
      <li>
        <svg viewBox="0 0 14 14" aria-hidden="true"><circle cx="7" cy="7" r="7" fill="var(--white)"/><circle cx="7" cy="7" r="4" fill="none" stroke="var(--sky)" stroke-width="0.9"/><ellipse cx="7" cy="7" rx="1.8" ry="4" fill="none" stroke="var(--sky)" stroke-width="0.8"/><path d="M3 7h8M3.6 5h6.8M3.6 9h6.8" stroke="var(--sky)" stroke-width="0.7"/></svg>
        www.nexoria.com
      </li>
    </ul>
  </section>

  <section class="card card--back">
    <svg class="card__waves" viewBox="0 0 507 303" preserveAspectRatio="none" aria-hidden="true">
      <path d="M2 0 C120 140 300 222 507 170 L507 0 Z" fill="var(--graphite)"/>
      <path d="M20 0 C135 134 305 213 507 163 L507 0 Z" fill="var(--card)"/>
      <path d="M29 0 C142 127 310 205 507 158 L507 0 Z" fill="var(--sky)"/>
    </svg>

    <div class="slogan">OUR COMPANY SLOGAN</div>
    <div class="wordmark">nexoria</div>
  </section>

</main>
</body>
</html>
```